Cafe Lindorf
Zielgruppe
Kaffeehaus mit Mehlspeisen, Mittagsmenüs und Abendöffnung zum Chillen
umliegende Firmenangestellt: für schnelles gutes preisgünstiges Mittagessen
umliegende Bewohner: zum Kaffee trinken/tratschen oder Essen/Trinken animiert werden
Touristen der umliegenden Hotels: traditionelle Wiener Küche mit Schnitzel und Apfelstrudel
Aufgabenstellung
wünsche mir eine durchgehende Linie
Logo
Visitenkarten - Werbung mit Promotion z.b. Melange + Hauskuchen
Postkarte für Werbung in Hotels - gleich aufgebaut wie Visitenkarten nur mehr Text
Frühstückskarte - mit Hauptseite
das Cafe/Restaurant gibt es seit einigen Jahrzehnten, hat jedoch einen Standortwechsel gemacht, und das Lokal ist moderner eingerichtet
Sollte alte Wiener Kaffeehauskunst kombiniert mit Moderner vermitteln.
Das Logo sollte zur Aussenbeschriftung passen, welche nicht gewechselt wird.

```html
<!DOCTYPE html>
<html lang="de">
<head>
<meta charset="utf-8">
<title>Cafe Lindorf – Geschäftsausstattung</title>
<link rel="stylesheet" href="https://fonts.googleapis.com/css2?family=Barlow:wght@400;600&family=Barlow+Condensed:wght@400;500&family=Source+Sans+3:wght@400&display=swap">
<style>
  :root {
    --plum: #5e1238;
    --gold: #c49a3c;
    --paper: #faf5e6;
    --ink: #1d1a17;
    --backdrop: #d9d9d6;
  }
  * { margin: 0; padding: 0; box-sizing: border-box; }
  html, body { width: 1200px; height: 848px; overflow: hidden; }
  body {
    position: relative;
    background: var(--backdrop);
    font-family: "Barlow", sans-serif;
    color: var(--ink);
  }

  /* Letterhead */
  .letterhead {
    position: absolute;
    left: 452px; top: 61px;
    width: 639px; height: 787px;
    background: var(--paper);
  }
  .letterhead .wordmark {
    position: absolute;
    right: 68px; top: 60px;
    font-size: 30px; font-weight: 600;
    color: var(--plum);
    letter-spacing: 0.4px;
  }
  .sender {
    position: absolute; left: 66px; top: 117px;
    font-size: 8.6px; letter-spacing: 0.2px; white-space: nowrap;
  }
  .sender strong { font-size: 9.6px; font-weight: 600; margin-right: 3px; letter-spacing: 0.1px; }
  .recipient {
    position: absolute; left: 66px; top: 131px;
    font-family: "Source Sans 3", sans-serif;
    font-style: normal;
    font-size: 11.5px; line-height: 13.6px;
  }
  .letter-rule {
    position: absolute; left: 71px; top: 287px;
    width: 20px; height: 1.5px; background: var(--ink);
  }
  .subject {
    position: absolute; left: 71px; top: 299px;
    font-size: 11.5px; font-weight: 600; line-height: 14.6px; letter-spacing: 0.2px;
  }
  .date {
    position: absolute; left: 389px; top: 299px;
    font-family: "Source Sans 3", sans-serif;
    font-size: 11.5px;
  }
  .letter-body {
    position: absolute; left: 71px; top: 358px;
    width: 530px;
    font-size: 11.2px; line-height: 14.7px;
  }
  .letter-body .greeting {
    font-family: "Source Sans 3", sans-serif;
    font-size: 11.5px; margin-bottom: 14.7px;
  }
  .letter-body h2 { font-size: 11.5px; font-weight: 600; line-height: 14.7px; letter-spacing: 0.2px; }
  .letter-body .copy { white-space: nowrap; letter-spacing: 0.35px; }
  .letter-footer-band {
    position: absolute; left: 13px; bottom: 0;
    width: 614px; height: 20px;
    background: var(--plum);
  }

  /* Business cards */
  .card {
    position: absolute; left: 195px;
    width: 280px; height: 181px;
  }
  .card-front { top: 414px; background: var(--paper); }
  .card-front .frame {
    position: absolute; inset: 9px 9px 9px 8px;
    border: 1.2px solid var(--gold);
    display: flex; align-items: center; justify-content: center;
  }
  .card-front .wordmark {
    font-size: 31px; font-weight: 600;
    color: var(--plum);
    letter-spacing: 0.4px;
    margin-bottom: 12px;
  }
  .card-back { top: 605px; height: 180px; background: var(--plum); }
  .card-back .inner {
    position: absolute; left: 17px; top: 15px; right: 17px; bottom: 17px;
    background: var(--paper);
    font-family: "Barlow Condensed", sans-serif;
    color: var(--plum);
  }
  .card-back .dot {
    position: absolute; left: 16px; top: 30px;
    width: 22px; height: 22px; border-radius: 50%;
    background: var(--plum);
  }
  .card-back .accent {
    position: absolute; left: 16px; top: 61px;
    width: 20px; height: 1.5px; background: var(--gold);
  }
  .card-back .person { position: absolute; left: 16px; top: 64px; }
  .card-back .person .name { font-size: 10px; font-weight: 500; line-height: 12px; }
  .card-back .person .role { font-size: 9px; line-height: 11px; }
  .card-back .contact {
    position: absolute; top: 112px;
    font-size: 7.6px; line-height: 10.6px; white-space: nowrap;
  }
  .contact.address { left: 16px; }
  .contact.phone { left: 85px; }
  .contact.web { left: 152px; }
</style>
</head>
<body>

  <section class="letterhead">
    <div class="wordmark">Cafe Lindorf</div>
    <p class="sender"><strong>Jakob Brenner</strong> Lindengasse 12 1070 Wien</p>
    <address class="recipient">
      Frau<br>Theresa Walcher<br>Kirchberggasse 8<br>1070 Wien
    </address>
    <div class="letter-rule"></div>
    <p class="subject">Rumendebis arum<br>Cumet resto corio</p>
    <p class="date">01.05.2015</p>
    <div class="letter-body">
      <p class="greeting">Sehr geehrte Frau Walcher<br>sehr geehrter Herr Pichler,</p>
      <p class="greeting">für die im Oktober 2012 bestellten Produkte erlauben wir uns zu berechnen:</p>
      <h2>Minulla volor sitaspe</h2>
      <p class="copy">rumendebis arum quis int quissus accab ipis deresed qui te earum restota tempossequi omnisciis<br>min rectur? Litati omnitis aute la verro te velic tem ipic tendit doloritis eatempo rumquia tiumque<br>ped mos aspidit emperum quam qui diam quunt, solupta tibeata tibusdant ius, quunte et, suntem-<br>quo earchic to eum faccuptas ex et est ommolup tatquia nos rehendelent.<br>Evendusam, sitius mint eatur adis comnihil eictotasi ini aut qui quia con pellorpos volupta quia<br>sus. Cumet resto corio. Lignam re la ipsae mosae il et quam, omnimet urepuda porrume nectio-<br>nem voluptat es poribus dendae eostota sim eum harum faces duci sit, volutat aut eturibusti is<br>rest, et mo consequia ipsum qui vent as dignim velende ndandit et volor atem quibus nonseque<br>pratem. Nemporati quibus</p>
    </div>
    <div class="letter-footer-band"></div>
  </section>

  <section class="card card-front">
    <div class="frame">
      <div class="wordmark">Cafe Lindorf</div>
    </div>
  </section>

  <section class="card card-back">
    <div class="inner">
      <div class="dot"></div>
      <div class="accent"></div>
      <div class="person">
        <div class="name">Jakob Brenner</div>
        <div class="role">Geschäftsführung</div>
      </div>
      <div class="contact address">Lindengasse 12<br>1070 Wien</div>
      <div class="contact phone">T 01 523 48 19<br>F 01 523 48 20</div>
      <div class="contact web">www.cafe-lindorf.at<br>info@cafe-lindorf.at</div>
    </div>
  </section>

</body>
</html>
```